Home Improvement Company in need of a "Banner & Billboard Design"

I'm Looking for a Banner design 4X6 With Company Logo, Phone Number, website, Credentials and services.. I picture a charcoal/matte background i also want to look like a house shape design i will upload the sample...

I'm looking for a Billboard design to target homeowners who need Roofing Services. I need logo, number, website, KTL, Credentials and a catchy title. i will like to use the same colors for branding

Target Market(s)

Homeowners, Investors,

Industry/Entity Type

Home Improvement

Font styles to use
Decorative

Colors
00a990
5c5c5c
333333

Requirements
Must have
• All Credentials, Phone number, website, logo, logo colors, services, Eye Catchy, Direct Message, Friendly feeling,
• (614) 372 - 9058
• Roofing Gutters Painting Pressure Washing Exterior Design
Nice to have
• A catchy title, A direct message to a homeowner looking for home improvement services. noticeable
Should not have
• not Busy, no

```html
<!DOCTYPE html>
<html lang="en">
<head>
<meta charset="UTF-8">
<title>Ridgeline Builders – Banner</title>
<link rel="stylesheet" href="https://fonts.googleapis.com/css2?family=Oswald:wght@500;600&display=swap">
<style>
  :root {
    --teal: #00a990;
    --teal-deep: #1f9a88;
    --charcoal: #363838;
    --slate: #5c5c5c;
    --ink: #333333;
    --white: #ffffff;
    --page: #ffffff;
    --badge-tone: #4a4c4c;
  }
  * { margin: 0; padding: 0; box-sizing: border-box; }
  html, body {
    width: 1044px; height: 1200px; overflow: hidden;
    background: var(--page);
  }
  .canvas { position: relative; width: 1044px; height: 1200px; }
  .banner {
    position: absolute; left: 0; top: 252px;
    width: 1044px; height: 696px;
    background: var(--charcoal);
    overflow: hidden;
    font-family: 'Oswald', sans-serif;
  }
  .banner-shapes { position: absolute; inset: 0; }
  .brand {
    position: absolute; left: 62px; top: 110px;
    display: flex; align-items: center; gap: 16px;
  }
  .brand-mark { width: 28px; height: 28px; background: var(--teal); }
  .brand-name {
    color: var(--teal); font-weight: 500;
    font-size: 44px; line-height: 1.05;
  }
  .credential-first {
    position: absolute; left: 700px; top: 136px;
    width: 82px; height: 132px; border-radius: 6px;
    background: var(--badge-tone);
  }
  .credential-second {
    position: absolute; left: 802px; top: 200px;
    width: 190px; height: 52px; border-radius: 4px;
    background: var(--badge-tone);
  }
  .phone {
    position: absolute; left: 0; right: 0; top: 356px;
    text-align: center; color: var(--white);
    font-weight: 600; font-size: 112px; line-height: 1;
  }
  .website {
    position: absolute; left: 0; right: 0; top: 490px;
    text-align: center; color: var(--teal);
    font-weight: 500; font-size: 38px; line-height: 1;
    letter-spacing: 0.32em; padding-left: 0.32em;
  }
  .services {
    position: absolute; left: 18px; top: 592px; height: 80px;
    display: flex; align-items: center;
    color: var(--white); font-weight: 500; font-size: 24px;
  }
  .contact-icons {
    position: absolute; left: 738px; top: 610px;
    display: flex; gap: 26px;
  }
  .contact-icons svg { width: 44px; height: 44px; }
</style>
</head>
<body>
<div class="canvas">
  <section class="banner">
    <svg class="banner-shapes" viewBox="0 0 1044 696" width="1044" height="696" aria-hidden="true">
      <rect x="0" y="0" width="1044" height="11" fill="var(--teal-deep)"/>
      <polygon points="786,0 1044,0 1044,216" fill="var(--teal-deep)"/>
      <polygon points="0,592 632,592 603,672 0,672" fill="var(--slate)"/>
      <polygon points="651,592 1044,592 1044,672 618,672" fill="var(--teal-deep)"/>
    </svg>

    <div class="brand">
      <span class="brand-mark"></span>
      <span class="brand-name">Ridgeline<br>Builders</span>
    </div>

    <div class="credential-first" role="img" aria-label="Accreditation credential badge"></div>
    <div class="credential-second" role="img" aria-label="Contractor certification badge"></div>

    <div class="phone">(614) 372 - 9058</div>
    <div class="website">www.RidgelineBuilders.com</div>

    <div class="services">Roofing Gutters Painting Pressure Washing Exterior Design</div>

    <div class="contact-icons">
      <svg viewBox="0 0 24 24" aria-label="Phone" role="img">
        <path d="M6.6 10.8a15 15 0 0 0 6.6 6.6l2.2-2.2c.3-.3.7-.4 1-.2 1.1.4 2.3.6 3.6.6.6 0 1 .4 1 1V20c0 .6-.4 1-1 1A17 17 0 0 1 3 4c0-.6.4-1 1-1h3.5c.6 0 1 .4 1 1 0 1.3.2 2.5.6 3.6.1.3 0 .7-.2 1z" fill="none" stroke="var(--ink)" stroke-width="1.8"/>
      </svg>
      <svg viewBox="0 0 24 24" aria-label="Website" role="img">
        <circle cx="12" cy="12" r="9" fill="none" stroke="var(--ink)" stroke-width="1.8"/>
        <path d="M3 12h18M12 3c3 3 3 15 0 18M12 3c-3 3-3 15 0 18" fill="none" stroke="var(--ink)" stroke-width="1.6"/>
      </svg>
      <svg viewBox="0 0 24 24" aria-label="Email" role="img">
        <rect x="3" y="6" width="18" height="12" fill="none" stroke="var(--ink)" stroke-width="1.8"/>
        <path d="M3 6l9 7 9-7" fill="none" stroke="var(--ink)" stroke-width="1.8"/>
      </svg>
    </div>
  </section>
</div>
</body>
</html>
```